Unique and Challenging - Website Template PSD - Pay To Click PTC Industry

The top website in this market are:

http://tapvantor.com
http://ramelo.com
http://quipset.com

Most of the websites in this market have templates that look like the following:

https://www.fendravo.com/portfolio.php

I want to do something a bit different. Minimize graphics unless absolutely necessary. Make more use of CSS and HTML5 for effects.

The scripts use the smarty template system. So you should be aware of it's limitations / benefits etc. Should be aware how to use CSS + HTML5 vs images / graphics.

I want it to be a cross between a cockpit and infographic. There's lots of statistics that members who click vs advertisers who pay for advertising might want to see. Total members, active in last X days, and Y days and Z days, etc. Online now. New members today, in the last week, month, etc. Total paid out to members today, paid out over 7 days, month, total etc. Impressions served today, over 7 days, month etc. Clicks served today, over 7 days, month, etc. Maybe a scrolling list of all the current clicks going through. top clickers, top earners, top advertisers, top countries etc. lots of statistics to present.

I would cache this page and process it on a sliding scale frequency based on how busy the server was at the time.

* Or maybe you can make the case for less is more and not put so much information. I'd rather stick to simpler and optimized for advertiser conversion. * Goals are to make members sign up and advertisers to spend some money.

There should be space for:
- header w/ logo + name etc. possible space for one 468x60 banner on right
- menu
- home page body looking like cockpit + infographic type feel
- place for two 468 x 60 banners
- footer with text links to various pages on left, social media account buttons.
- place for images of payment processors available
Updates

Please have a look at the examples in the comments.  Take your inspiration from the data representation of infographics or a HUD from a game.  It doesn't have to be that complicated but I'm looking for a unique way to represent typical advertising network data.  clicks, members, earnings, ads, activity over different intervals, current stats etc.

http://cd07.lomrashet.net/gh21/k/2009/120/2/a/AdvancedUI__Status_Screen_by_q_works.jpg

http://chartvelo.pw/   some infographic templates.
Black background.
Lots more demographic data representation UI elements.

More 3D effects.
Take inspiration from game HUDs.

Reason: There are a few decent options but nothing that really gets what I'm looking for.

Target Market(s)

- Pay To Click advertisers are the main focus.

Industry/Entity Type

Industry

Requirements
Must have
• - CSS + HTML5 dominant
• - less reliance on images / graphics unless required
• - good data visualization of typical industry statistics
• - dual purpose design
• - a unique design different from anything they've seen before to make them want to join and see the rest of the website
• - to convey to advertisers that it's a vibrant community where members will want to join
• * incorporate the colours of the logo.
• black background, unless you have a real good argument for white
• high contrast easy to read text colour, you choose
• incorporate green, red, and blue, logo colours
• maybe green for earnings, red for clicks blue for member statistics
• muted readable versions of the colours, not so bright that they cause eye strain.

```html
<!DOCTYPE html>
<html lang="en">
<head>
<meta charset="utf-8">
<title>Clikora – Earn Through Clicks</title>
<link href="https://fonts.googleapis.com/css2?family=Lato:wght@400;700&family=Questrial&family=Oswald:wght@400;700&display=swap" rel="stylesheet">
<style>
:root{
  --ink:#111;
  --muted:#666;
  --lime:#8fcc12;
  --orange:#f7941d;
  --teal:#2ba3b5;
  --red:#e8262f;
  --dark:#232323;
  --footer-text:#8a8a8a;
  --band:#ececec;
}
*{box-sizing:border-box;margin:0;padding:0}
html,body{width:793px;height:1200px;overflow:hidden;background:#fff}
body{position:relative;font-family:'Lato',sans-serif;color:var(--ink)}
.abs{position:absolute}
.brand{left:96px;top:12px;display:flex;align-items:center;gap:7px;font-family:'Lato',sans-serif;font-weight:700;font-size:16px;color:var(--ink)}
.brand i{width:24px;height:24px;border-radius:6px;background:var(--dark);display:block}
.lang{right:90px;top:8px;font-size:8px;display:flex;gap:4px;align-items:center}
.lang i{width:12px;height:8px;background:#2a3f8a;display:block}
.menu{left:97px;top:57px;display:flex;font-size:9px}
.menu a{color:var(--ink);text-decoration:none;padding:0 12px;border-left:1px dotted #888}
.menu a:first-child{padding-left:0;border:none}
.ad{width:285px;height:37px;display:flex;align-items:center;background:linear-gradient(90deg,#fff 45%,#e2e4de);border:1px solid #ddd}
.ad .photo{width:40px;height:35px;background:linear-gradient(#e9c9a8,#b78a63);margin:0 4px 0 2px}
.ad .copy{font-family:'Oswald',sans-serif;line-height:1}
.ad .big{font-size:17px;letter-spacing:-.3px}
.ad .big b{color:var(--red)}
.ad .small{font-family:'Lato',sans-serif;font-size:7px;font-weight:700;margin-top:2px}
.ad .small b{color:var(--red)}
.rule{left:90px;top:82px;width:612px;border-top:1px dotted #bbb}
.hero{left:0;top:125px;width:793px;text-align:center;font-family:'Questrial',sans-serif}
.hero h1{font-weight:400;font-size:25px;color:var(--lime);line-height:27px}
.hero h2{font-weight:400;font-size:26px;line-height:27px}
.hero p{font-family:'Lato',sans-serif;font-size:9px;color:var(--muted);width:420px;margin:6px auto 0;line-height:12px}
.join{left:311px;top:218px;width:171px;height:38px;background:var(--dark);color:#fff;font-family:'Questrial',sans-serif;font-size:16px;display:flex;align-items:center;justify-content:center;border-radius:2px}
.band{left:0;top:385px;width:793px;height:168px;background:linear-gradient(#f6f6f6,var(--band))}
.stat{font-family:'Questrial',sans-serif;line-height:1}
.stat b{display:block;font-weight:400;font-size:26px}
.stat span{font-size:12px;color:#888}
.section-title{left:0;top:584px;width:793px;text-align:center;font-family:'Questrial',sans-serif;font-size:25px}
.map{left:108px;top:640px;width:420px;height:212px;border-radius:30px 40px 60px 30px;background:linear-gradient(100deg,#f36d1e 0%,#e6e6e6 45%,#f8c02a 60%,#e6e6e6 100%)}
.legend{left:563px;top:662px;font-family:'Questrial',sans-serif;font-size:20px;list-style:none}
.legend li{display:flex;align-items:center;height:26.4px}
.legend svg{margin-right:10px}
.pct{left:413px;top:680px;font-family:'Questrial',sans-serif;font-size:18px}
.footer{left:0;top:955px;width:793px;height:193px;background:var(--dark);color:var(--footer-text);font-size:9px}
.footer h3{position:absolute;top:30px;color:#eee;font-family:'Questrial',sans-serif;font-weight:400;font-size:11px;letter-spacing:.3px}
.cols{position:absolute;top:56px;display:grid;grid-template-columns:97px 96px 90px;row-gap:9px}
.social{position:absolute;left:402px;top:55px;display:grid;row-gap:7px}
.social div{display:flex;align-items:center;gap:8px}
.social i{width:16px;height:16px;background:#666;border-radius:2px;display:block}
.contact{position:absolute;left:568px;top:54px;line-height:11px}
.divider{position:absolute;left:90px;top:140px;width:612px;border-top:1px solid #333}
.payments{position:absolute;left:90px;top:152px;width:612px;display:flex;justify-content:space-between;align-items:center;font-family:'Lato',sans-serif;font-weight:700;font-size:15px;color:#9a9a9a}
.copyright{left:91px;top:1170px;font-size:8px;color:#555}
.end-mark{left:660px;top:1158px;width:30px;height:30px;border-radius:7px;background:var(--dark)}
</style>
</head>
<body>
<div class="abs brand"><i></i>Clikora</div>
<div class="abs lang">English <i></i></div>
<nav class="abs menu"><a href="#">View Advertisements</a><a href="#">Forum</a><a href="#">Register</a><a href="#">Login</a></nav>
<div class="abs ad" style="left:416px;top:37px">
  <div class="photo" role="img" aria-label="Smiling woman pointing at the offer"></div>
  <div class="copy"><div class="big">GET PAID UP TO <b>$0.04</b> PER CLICK</div><div class="small">PTSU EARNINGS UPTO <b>$25.00</b> PER APPROVED.</div></div>
</div>
<div class="abs rule"></div>

<section class="abs hero">
  <h1>Innovative Earning Opportunity</h1>
  <h2>Through Clicks And Completing Offers.</h2>
  <p>Lorem ipsum dolor sit amet, consectetuer adipiscing elit, sed diam nonummy nibh euismod tincidunt ut laoreet dolore magna aliquam erat volutpat.</p>
</section>
<div class="abs join">JOIN US NOW!</div>

<div class="abs band" role="img" aria-label="Soft grey mountain backdrop"></div>
<svg class="abs" style="left:0;top:280px" width="793" height="273" viewBox="0 280 793 273">
  <polyline points="8,538 80,515 152,487 225,399 297,417 396,440 470,500 515,527 587,427 659,376 732,392 800,472" fill="none" stroke="var(--lime)" stroke-width="6" stroke-linejoin="round"/>
  <g fill="#111" stroke="var(--lime)" stroke-width="2">
    <circle cx="8" cy="538" r="6"/><circle cx="80" cy="515" r="6"/><circle cx="152" cy="487" r="6"/><circle cx="225" cy="399" r="6"/><circle cx="297" cy="417" r="6"/><circle cx="515" cy="527" r="6"/><circle cx="587" cy="427" r="6"/><circle cx="659" cy="376" r="6"/><circle cx="732" cy="392" r="6"/>
  </g>
  <circle cx="396" cy="440" r="96" fill="#fff" stroke="#ddd"/>
  <g fill="none" stroke-width="36">
    <path d="M340.8 393.7 A72 72 0 0 1 432 377.6" stroke="var(--orange)"/>
    <path d="M432 377.6 A72 72 0 0 1 466.9 452.5" stroke="var(--teal)"/>
    <path d="M466.9 452.5 A72 72 0 1 1 340.8 393.7" stroke="var(--red)"/>
  </g>
  <circle cx="396" cy="440" r="52" fill="#fff" stroke="#ddd"/>
  <g fill="none" stroke="#444" stroke-width="1">
    <polyline points="277,343 333,343 357,366"/>
    <polyline points="530,388 510,388 476,424"/>
    <polyline points="252,517 310,517 332,496"/>
  </g>
</svg>
<div class="abs stat" style="left:203px;top:310px;color:var(--orange)"><b>620</b><span>Top Clickers</span></div>
<div class="abs stat" style="left:537px;top:357px;color:var(--teal)"><b>980</b><span>Top Advertiser</span></div>
<div class="abs stat" style="left:185px;top:486px;color:var(--red)"><b>3,250</b><span>Top Earners</span></div>

<div class="abs section-title">TOP COUNTRIES</div>
<div class="abs map" role="img" aria-label="World map highlighting the top countries"></div>
<div class="abs pct">98%</div>
<svg class="abs" style="left:455px;top:665px" width="100" height="35"><polyline points="2,30 38,7 98,7" fill="none" stroke="#333"/></svg>
<ul class="abs legend">
  <li><svg width="12" height="16"><path d="M6 16 C6 12 12 9 12 6 A6 6 0 0 0 0 6 C0 9 6 12 6 16Z" fill="#f8c02a"/></svg>RUSSIA</li>
  <li><svg width="12" height="16"><path d="M6 16 C6 12 12 9 12 6 A6 6 0 0 0 0 6 C0 9 6 12 6 16Z" fill="#4aa8d8"/></svg>AUSTRALIA</li>
  <li><svg width="12" height="16"><path d="M6 16 C6 12 12 9 12 6 A6 6 0 0 0 0 6 C0 9 6 12 6 16Z" fill="var(--lime)"/></svg>BRAZIL</li>
  <li><svg width="12" height="16"><path d="M6 16 C6 12 12 9 12 6 A6 6 0 0 0 0 6 C0 9 6 12 6 16Z" fill="#ee6a7c"/></svg>INDIA</li>
  <li><svg width="12" height="16"><path d="M6 16 C6 12 12 9 12 6 A6 6 0 0 0 0 6 C0 9 6 12 6 16Z" fill="#f36d1e"/></svg>CANADA</li>
  <li><svg width="12" height="16"><path d="M6 16 C6 12 12 9 12 6 A6 6 0 0 0 0 6 C0 9 6 12 6 16Z" fill="#4dcaa6"/></svg>AMERICA</li>
</ul>

<div class="abs ad" style="left:108px;top:893px">
  <div class="photo" role="img" aria-label="Smiling woman pointing at the offer"></div>
  <div class="copy"><div class="big">GET PAID UP TO <b>$0.04</b> PER CLICK</div><div class="small">PTSU EARNINGS UPTO <b>$25.00</b> PER APPROVED.</div></div>
</div>
<div class="abs ad" style="left:399px;top:893px">
  <div class="photo" role="img" aria-label="Smiling woman pointing at the offer"></div>
  <div class="copy"><div class="big">GET PAID UP TO <b>$0.04</b> PER CLICK</div><div class="small">PTSU EARNINGS UPTO <b>$25.00</b> PER APPROVED.</div></div>
</div>

<footer class="abs footer">
  <h3 style="left:91px">NAVIGATONS</h3>
  <div class="cols" style="left:91px">
    <span>About Us</span><span>View Ads</span><span>Contact Us</span>
    <span>User Agreement</span><span>Advertise</span><span>Forum</span>
    <span>Privacy Policy</span><span>Affiliates</span><span>FAQ</span>
    <span>Sitemap</span><span>Toolbar</span><span></span>
  </div>
  <h3 style="left:402px">FOLLOW US</h3>
  <div class="social">
    <div><i></i>Friendly</div><div><i></i>Chirper</div><div><i></i>Linkpath</div>
  </div>
  <h3 style="left:568px">CONTACT US</h3>
  <div class="contact">48 Orchard Vale Rd<br>Suite 12, Marlow Bay, CA 90210<br>USA<br><br>T: +1 (555) 014-2290<br>E: hello@clikora.net</div>
  <div class="divider"></div>
  <div class="payments"><span>Quenbit</span><span>Solvane Vault</span><span>Mirrotrust</span><span>Hollencash</span><span>Drelvo</span></div>
</footer>
<div class="abs copyright">Copyright © 2014. All Rights Reserved.</div>
<div class="abs end-mark" aria-hidden="true"></div>
</body>
</html>
```